We are a new towing and recovery company starting out in Calhan, CO. We do not want anything generic, we are looking to stand out. we will be doing towing for motorcycles to straight trucks we will have a rollback a 16-ton wrecker and a service vehicle with a wheel lift attached to tow small sized vehicles. We will also be doing roadside services which include lock-out, fuel delivery, jumpstarts, tire changes, and minor auto repair. we will be providing a quality and fast service also customer service will be one of main focuses.

Industry/Entity Type

Wheel

Contact Information for Business Card

Brindle Ridge Towing and Recovery, Dale Hoskin, Owner, 48210 S. Ferrow Road, Dunmere, ST 00000 555-218-6497 Phone 555-218-6532 Fax www.brindleridgetow.example

```html
<!DOCTYPE html>
<html lang="en">
<head>
<meta charset="utf-8">
<title>Brindle Ridge Towing and Recovery – Business Card</title>
<link rel="stylesheet" href="https://fonts.googleapis.com/css2?family=Arimo:wght@400;700&family=Roboto+Slab:wght@700&family=Archivo+Black&display=swap">
<style>
  :root {
    --page-bg: #eeeeee;
    --card-white: #ffffff;
    --accent-red: #e0201b;
    --plate-dark: #151515;
    --plate-mid: #3a3a3a;
    --ink-black: #111111;
    --text-white: #ffffff;
    --divider: #8a8a8a;
    --truck-red: #c9261c;
    --truck-grey: #9aa0a6;
  }
  * { box-sizing: border-box; margin: 0; padding: 0; }
  html, body { width: 1200px; height: 900px; overflow: hidden; }
  body {
    background: var(--page-bg);
    font-family: "Arimo", Arial, sans-serif;
    position: relative;
  }
  .business-card {
    position: absolute;
    left: 75px; top: 150px;
    width: 1050px; height: 600px;
    border-radius: 34px;
    overflow: hidden;
    background: var(--card-white);
    box-shadow: 0 10px 30px rgba(0,0,0,0.18);
  }
  .brand-strip {
    position: absolute; left: 0; top: 0;
    width: 100%; height: 212px;
    background: var(--card-white);
  }
  .truck-illustration {
    position: absolute; left: 22px; top: 40px;
    width: 240px; height: 160px;
    border-radius: 14px;
    background: linear-gradient(160deg, var(--truck-red) 0%, #8f1e16 45%, var(--truck-grey) 100%);
  }
  .company-name {
    position: absolute; left: 280px; top: 96px;
    font-family: "Roboto Slab", Georgia, serif;
    font-weight: 700;
    font-size: 40px;
    letter-spacing: -0.5px;
    color: var(--ink-black);
    white-space: nowrap;
  }
  .tagline-band {
    position: absolute; left: 0; top: 212px;
    width: 100%; height: 28px;
    background: var(--accent-red);
    display: flex; align-items: center; justify-content: center;
  }
  .tagline {
    font-family: "Archivo Black", Arial, sans-serif;
    font-size: 22px;
    letter-spacing: 6px;
    color: var(--ink-black);
    text-transform: uppercase;
    line-height: 1;
  }
  .plate-area {
    position: absolute; left: 0; top: 240px;
    width: 100%; height: 360px;
    background: radial-gradient(ellipse at 50% 40%, var(--plate-mid) 0%, var(--plate-dark) 75%);
  }
  .owner {
    position: absolute; left: 40px; top: 268px;
  }
  .owner-name {
    font-size: 34px; color: var(--accent-red); line-height: 1.2;
  }
  .owner-title {
    font-size: 26px; color: var(--text-white); line-height: 1.3;
  }
  .divider {
    position: absolute; left: 292px; top: 262px;
    width: 2px; height: 300px;
    background: var(--divider);
  }
  .contact-list {
    position: absolute; left: 308px; top: 262px;
    list-style: none;
  }
  .contact-item {
    display: flex; align-items: center;
    height: 44px;
    font-size: 29px;
    color: var(--text-white);
    white-space: nowrap;
  }
  .contact-item.continued { padding-left: 40px; }
  .contact-icon {
    width: 30px; height: 30px;
    margin-right: 10px;
    flex: none;
  }
</style>
</head>
<body>
  <div class="business-card">
    <div class="brand-strip">
      <div class="truck-illustration" role="img" aria-label="Illustration of a red rollback tow truck"></div>
      <div class="company-name">Brindle Ridge Towing and Recovery</div>
    </div>

    <div class="tagline-band">
      <span class="tagline">Big or small, we do them all</span>
    </div>

    <div class="plate-area" role="img" aria-label="Dark diamond plate steel texture"></div>

    <div class="owner">
      <div class="owner-name">Dale Hoskin</div>
      <div class="owner-title">Owner/Operator</div>
    </div>

    <div class="divider"></div>

    <ul class="contact-list">
      <li class="contact-item">
        <svg class="contact-icon" viewBox="0 0 30 30" aria-hidden="true"><rect x="9" y="3" width="12" height="24" rx="2" fill="none" stroke="#e0201b" stroke-width="2.5"/><circle cx="15" cy="23" r="1.5" fill="#e0201b"/></svg>
        555-218-6475
      </li>
      <li class="contact-item">
        <svg class="contact-icon" viewBox="0 0 30 30" aria-hidden="true"><path d="M8 4 l5 5 -3 3 c2 4 4 6 8 8 l3 -3 5 5 -3 4 c-9 0 -19 -10 -19 -19z" fill="#e0201b"/></svg>
        555-218-6497
      </li>
      <li class="contact-item">
        <svg class="contact-icon" viewBox="0 0 30 30" aria-hidden="true"><rect x="4" y="12" width="22" height="13" rx="2" fill="#e0201b"/><rect x="9" y="4" width="12" height="9" fill="none" stroke="#e0201b" stroke-width="2"/><rect x="8" y="16" width="14" height="2" fill="#151515"/></svg>
        555-218-6532
      </li>
      <li class="contact-item">
        <svg class="contact-icon" viewBox="0 0 30 30" aria-hidden="true"><rect x="3" y="7" width="24" height="16" rx="2" fill="#e0201b"/><path d="M3 8 l12 9 12 -9" fill="none" stroke="#151515" stroke-width="2"/></svg>
        brindleridge_tow
      </li>
      <li class="contact-item">
        <svg class="contact-icon" viewBox="0 0 30 30" aria-hidden="true"><circle cx="15" cy="15" r="11" fill="none" stroke="#e0201b" stroke-width="2.5"/><ellipse cx="15" cy="15" rx="5" ry="11" fill="none" stroke="#e0201b" stroke-width="2"/><line x1="4" y1="15" x2="26" y2="15" stroke="#e0201b" stroke-width="2"/></svg>
        www.brindleridgetow.example
      </li>
      <li class="contact-item">
        <svg class="contact-icon" viewBox="0 0 30 30" aria-hidden="true"><path d="M3 15 L15 4 L27 15 H23 V26 H17 V19 H13 V26 H7 V15z" fill="#e0201b"/></svg>
        48210 S. Ferrow Road,
      </li>
      <li class="contact-item continued">Dunmere, ST 00000</li>
    </ul>
  </div>
</body>
</html>
```